FUN WEBSITE NEEDED FOR NEW ACCESSORY PRINTING COMPANY

NOTE: This is Website Design Only - No coding required

PLEASE SUBMIT YOUR DESIGNS RIGHT AWAY AS WE WANT TO PICK A WINNER ASAP!

Hi,

We are looking for a vibrant and hip website for a new emerging industry that allows us to personalize cell phone covers and many other items with our unique printing ability.

Our site must be hip and vibrant, as our audience is high schoolers and teens for the most part.

The site should be simple and straight forward while at the same time be of high visual quality.

This will be an e-commerce site that will sell around 10 products.

Please provide designs for a great looking site to help us sell our products.

You will find our logo attached. Here is a link to our catalogue so you can get an idea of what we do. Again Cell Phone Covers will be our main priority so please focus on that.

https://www.filevault-example.net/s/qetumaxlor7261/SnapGlo%20Catalog%2011x17.pdf

Thanks!
Todd

Target Market(s)

The target market is high schoolers and teens.

Additional target market is Collage kids

Sports Teams

Industry/Entity Type

Cell Phone

Font styles to use
Sans Serif

Requirements
Must have
• Clean look
Ecommerce
Horizontal menu
Showing cell phone printing from catalogue
Follow Logo Colors
Should not have
• Cluttery design
Hard to read see
Not clean

```html
<!DOCTYPE html>
<html lang="en">
<head>
<meta charset="utf-8">
<title>SnapGlo – Custom Printed Accessories</title>
<link href="https://fonts.googleapis.com/css2?family=Open+Sans:wght@400;600;700&display=swap" rel="stylesheet">
<style>
:root{
  --orange:#f7941d;
  --orange-light:#ffa41c;
  --red:#d7191f;
  --ink:#1e1e1e;
  --text:#333;
  --muted:#666;
  --line:#d8d8d8;
  --topbar:#9b9b9b;
  --footer:#e9e9e9;
  --bottom:#bdbdbd;
}
*{margin:0;padding:0;box-sizing:border-box}
html,body{width:949px;height:1200px;overflow:hidden}
body{font-family:"Open Sans",Arial,sans-serif;color:var(--text);background:#fff;position:relative}
.abs{position:absolute}
a{color:inherit;text-decoration:none}

.top-bar{left:0;top:0;width:949px;height:19px;background:var(--topbar)}
.top-links{right:66px;top:0;display:flex;font-size:8.5px;color:#fff;height:19px;align-items:center}
.top-links a{padding:0 8px;border-left:1px solid #b9b9b9;line-height:19px}
.top-links a:first-child{border-left:none}

.brand{left:86px;top:44px;display:flex;align-items:center;gap:8px}
.brand-dot{width:30px;height:30px;border-radius:50%;background:var(--red)}
.brand-name{font-size:30px;font-weight:700;color:var(--red)}

.contact{display:flex;align-items:center;gap:6px;top:64px}
.contact small{display:block;font-size:9px;color:var(--muted);line-height:11px}
.contact strong{display:block;font-size:14px;color:var(--ink);line-height:16px;font-weight:600}

.cart{right:88px;top:36px;font-size:9.5px;display:flex;align-items:center;gap:5px}
.cart b{font-weight:600}
.cart .checkout{color:var(--orange);margin-left:3px}

.search{left:625px;top:65px;width:236px;height:30px;border:1px solid var(--line);display:flex}
.search span{flex:1;font-size:9.5px;color:#999;padding:9px 12px}
.search b{width:62px;border-left:1px solid var(--line);background:#f4f4f4;font-size:11px;display:flex;align-items:center;justify-content:center;color:var(--ink)}

.main-nav{left:0;top:109px;width:949px;height:27px;background:linear-gradient(#ffa71a,#f58e10)}
.main-nav ul{list-style:none;display:flex;margin-left:86px;height:27px;align-items:center}
.main-nav li{color:#fff;font-weight:700;font-size:11px;padding:0 8px;border-left:1px solid #fbbf6a;line-height:12px}
.main-nav li:first-child{padding-left:0;border-left:none}

.hero{left:0;top:136px;width:949px;height:296px;background:radial-gradient(ellipse at 55% 40%,#fafafa,#e3e3e3 80%);border-bottom:1px solid #cfcfcf}
.hero h1{left:85px;top:54px;font-size:25px;line-height:33px;color:var(--ink);font-weight:700;position:absolute}
.hero p{left:85px;top:117px;width:270px;font-size:12px;line-height:21.5px;color:var(--ink);position:absolute}
.hero .cta{left:85px;top:191px;width:104px;height:31px;background:var(--red);border-radius:2px;color:#fff;font-weight:700;font-size:12px;display:flex;align-items:center;justify-content:center;position:absolute}
.hero .dots{left:89px;top:251px;display:flex;gap:4px;position:absolute}
.dots i{width:9px;height:9px;border-radius:50%;background:#aaa;display:block}
.hero-art{left:480px;top:42px;width:372px;height:217px;position:absolute}

.perk{top:443px;width:188px;height:85px;border:1px solid var(--line);background:#fff}
.perk .ico{position:absolute;left:13px;top:12px;width:61px;height:61px;border-radius:50%;border:1px solid #ccc;display:flex;align-items:center;justify-content:center}
.perk h3{position:absolute;right:14px;top:17px;font-size:21px;font-weight:400;color:var(--ink)}
.perk span{position:absolute;right:14px;top:47px;font-size:11px;color:var(--muted)}

.rule{left:0;top:540px;width:949px;height:1px;background:#e2e2e2}
.section-title{left:0;width:949px;text-align:center;font-weight:600;color:var(--ink)}

.product{top:588px;width:188px;height:245px;border:1px solid var(--line);background:#fff}
.product .pic{position:absolute;left:20px;top:20px;width:146px;height:137px;border-radius:6px}
.product p{position:absolute;left:13px;top:167px;font-size:10.5px;line-height:16px;color:var(--ink)}
.product .more{position:absolute;left:13px;top:208px;width:67px;height:22px;background:linear-gradient(#ffa71a,#f58e10);border:1px solid #e07f00;border-radius:2px;color:#fff;font-size:10px;display:flex;align-items:center;justify-content:center}
.arrow{top:700px;width:21px;height:21px;border-radius:50%;background:#444;display:flex;align-items:center;justify-content:center}

.shadow-rule{left:120px;top:859px;width:710px;height:3px;background:radial-gradient(ellipse,#cfcfcf,transparent 70%)}

.quote{width:400px;height:110px}
.quote .avatar{position:absolute;left:0;top:0;width:78px;height:78px;border-radius:50%;background:radial-gradient(circle at 50% 40%,#d9b79b,#6f6d6a 70%)}
.quote p{position:absolute;left:94px;top:5px;width:310px;font-size:10.3px;line-height:16px;color:var(--ink)}
.quote b{position:absolute;left:94px;top:76px;font-size:10.5px;color:var(--ink);white-space:nowrap}
.quote span{position:absolute;left:94px;top:92px;font-size:10.5px;color:var(--muted);white-space:nowrap}
.t-dots{left:456px;top:1014px;display:flex;gap:6px}
.t-dots i{width:10px;height:10px;border-radius:50%;background:#bbb;display:block}
.t-dots i:first-child{background:var(--orange)}

.footer{left:0;top:1041px;width:949px;height:124px;background:var(--footer)}
.f-col{top:1051px}
.f-col h4{font-size:11px;font-weight:700;color:var(--ink);margin-bottom:3px}
.f-col li{list-style:none;font-size:9.5px;line-height:18.3px;color:#444}
.offer{left:616px;top:1075px;display:flex;align-items:center;gap:10px}
.offer span{color:var(--red);font-weight:700;font-size:13px;line-height:13px;width:80px}
.social{left:775px;top:1051px}
.social h4{font-size:11px;font-weight:700;color:var(--ink);margin-bottom:6px}
.social li{list-style:none;display:flex;align-items:center;gap:9px;font-size:9.5px;color:#444;height:30px}
.social li i{width:26px;height:26px;border-radius:50%;background:var(--orange);display:block}
.bottom-bar{left:0;top:1165px;width:949px;height:35px;background:var(--bottom);font-size:8px;color:#333;display:flex;align-items:center;justify-content:center}
</style>
</head>
<body>

<div class="abs top-bar"></div>
<nav class="abs top-links"><a>Login</a><a>Signup</a><a>My Account</a><a>Order Status</a><a>Wish List</a></nav>

<div class="abs brand"><i class="brand-dot"></i><span class="brand-name">SnapGlo</span></div>

<div class="abs contact" style="left:308px">
  <svg width="24" height="28" viewBox="0 0 24 28"><path d="M5 3c2-1 3 0 4 2l2 4c1 2 0 3-1 4l-1 1c1 3 3 6 6 7l1-1c1-1 2-1 4 0l2 2c1 1 1 3-1 4-3 2-7 1-11-3S1 11 2 7c0-2 1-3 3-4z" fill="#f7941d"/><path d="M14 5a7 7 0 0 1 6 6M14 1a11 11 0 0 1 9 9" stroke="#f7941d" stroke-width="1.6" fill="none"/></svg>
  <div><small>talk to a real person</small><strong>(555) 218 340</strong></div>
</div>
<div class="abs contact" style="left:462px">
  <svg width="30" height="28" viewBox="0 0 30 28"><rect x="1" y="6" width="20" height="14" rx="1" fill="none" stroke="#f7941d" stroke-width="2.4"/><rect x="7" y="20" width="8" height="3" fill="#f7941d"/><rect x="4" y="23" width="14" height="2" fill="#f7941d"/><circle cx="22" cy="8" r="7" fill="#f7941d"/><circle cx="19" cy="8" r="1" fill="#fff"/><circle cx="22" cy="8" r="1" fill="#fff"/><circle cx="25" cy="8" r="1" fill="#fff"/></svg>
  <div><small>chat with a real person</small><strong>LIVE CHAT NOW</strong></div>
</div>

<div class="abs cart">
  <svg width="20" height="14" viewBox="0 0 20 14"><path d="M0 1h4l2 8h11l2-6H5" fill="none" stroke="#888" stroke-width="1.6"/><path d="M5 3h14l-2 6H7z" fill="#888"/><circle cx="8" cy="12" r="1.5" fill="#888"/><circle cx="16" cy="12" r="1.5" fill="#888"/></svg>
  <span>0Items <b>($0.00)</b></span><a class="checkout">Checkout</a>
</div>

<div class="abs search"><span>Search Keyword</span><b>SEARCH</b></div>

<nav class="abs main-nav"><ul><li>HOME</li><li>ABOUT US</li><li>CELL PHONE&nbsp; COVERS</li><li>TSHIRTS</li><li>BAGS</li><li>CUPS</li><li>KIDS &amp; BABY</li><li>OFFICE PRODUCTS</li><li>ACCESSORIES</li></ul></nav>

<section class="abs hero">
  <h1>CUSTOM<br>CELL PHONE COVERS</h1>
  <p>Lorem Ipsum is simply dummy text of the<br>printing and typesetting industry. Lorem<br>Ipsum has been the industry's standard.</p>
  <a class="cta">LEARN MORE</a>
  <div class="dots"><i></i><i></i><i></i></div>
  <svg class="hero-art" viewBox="0 0 372 217" role="img" aria-label="Row of custom printed phone covers showing family, pet and winter photos">
    <defs>
      <linearGradient id="ph1" x1="0" y1="0" x2="0" y2="1"><stop offset="0" stop-color="#6e9a5a"/><stop offset="1" stop-color="#c9a58b"/></linearGradient>
      <linearGradient id="ph2" x1="0" y1="0" x2="0" y2="1"><stop offset="0" stop-color="#7fa8d6"/><stop offset="1" stop-color="#c9b7a8"/></linearGradient>
      <linearGradient id="ph3" x1="0" y1="0" x2="0" y2="1"><stop offset="0" stop-color="#9a9ea2"/><stop offset="1" stop-color="#5e6266"/></linearGradient>
      <linearGradient id="ph4" x1="0" y1="0" x2="0" y2="1"><stop offset="0" stop-color="#5b9ad0"/><stop offset="1" stop-color="#e6eef5"/></linearGradient>
    </defs>
    <rect x="275" y="2" width="95" height="190" rx="10" fill="#e9ded6"/>
    <rect x="2" y="4" width="98" height="190" rx="10" fill="url(#ph1)" stroke="#333" stroke-width="2"/>
    <rect x="82" y="12" width="98" height="195" rx="10" fill="url(#ph2)" stroke="#222" stroke-width="2"/>
    <rect x="164" y="20" width="98" height="195" rx="10" fill="url(#ph3)" stroke="#ccc" stroke-width="2"/>
    <rect x="244" y="26" width="98" height="190" rx="10" fill="url(#ph4)" stroke="#333" stroke-width="2"/>
  </svg>
</section>

<div class="abs perk" style="left:86px">
  <div class="ico"><svg width="36" height="36" viewBox="0 0 36 36"><path d="M18 3h14v14L16 33 3 20z" fill="#d7191f"/><circle cx="26" cy="9" r="2.5" fill="#fff"/><text x="16" y="22" fill="#fff" font-size="8" font-weight="700" font-family="Open Sans,sans-serif" transform="rotate(-45 16 20)" text-anchor="middle">SALE</text></svg></div>
  <h3>Special</h3><span>Discount Items</span>
</div>
<div class="abs perk" style="left:281px">
  <div class="ico"><svg width="40" height="28" viewBox="0 0 40 28"><rect x="1" y="3" width="25" height="17" fill="#d7191f"/><path d="M27 8h7l5 6v6H27z" fill="#d7191f"/><circle cx="9" cy="22" r="4" fill="#d7191f" stroke="#fff" stroke-width="1.5"/><circle cx="32" cy="22" r="4" fill="#d7191f" stroke="#fff" stroke-width="1.5"/><text x="13.5" y="15" fill="#fff" font-size="8" font-weight="700" font-family="Open Sans,sans-serif" text-anchor="middle">FREE</text></svg></div>
  <h3>Shipping</h3><span>Free</span>
</div>
<div class="abs perk" style="left:477px">
  <div class="ico"><svg width="34" height="34" viewBox="0 0 34 34"><path d="M7 17a10 10 0 0 1 20 0" fill="none" stroke="#d7191f" stroke-width="3"/><rect x="4" y="15" width="6" height="9" rx="2" fill="#d7191f"/><rect x="24" y="15" width="6" height="9" rx="2" fill="#d7191f"/><path d="M27 24q0 6-8 6" fill="none" stroke="#d7191f" stroke-width="2"/><path d="M6 34q0-7 11-7t11 7z" fill="#d7191f"/></svg></div>
  <h3>Support</h3><span>Customer Service</span>
</div>
<div class="abs perk" style="left:673px">
  <div class="ico"><svg width="30" height="40" viewBox="0 0 30 40"><text x="15" y="34" fill="#d7191f" font-size="40" font-weight="700" font-family="Open Sans,sans-serif" text-anchor="middle">?</text></svg></div>
  <h3>About Us</h3><span>Click Here</span>
</div>

<div class="abs rule"></div>
<h2 class="abs section-title" style="top:553px;font-size:17.5px">Featured Products</h2>

<div class="abs arrow" style="left:57px"><svg width="8" height="8" viewBox="0 0 8 8"><path d="M6 0v8L1 4z" fill="#fff"/></svg></div>
<div class="abs arrow" style="left:871px"><svg width="8" height="8" viewBox="0 0 8 8"><path d="M2 0v8l5-4z" fill="#fff"/></svg></div>

<article class="abs product" style="left:86px">
  <div class="pic" role="img" aria-label="Printed phone cover with a group photo" style="background:linear-gradient(135deg,#7ea6c8,#d8cfc4 60%,#3b3b3b)"></div>
  <p>Custom Cell Phone Covers<br>AF USM Lens</p><a class="more">More Info</a>
</article>
<article class="abs product" style="left:281px">
  <div class="pic" role="img" aria-label="White photo mug with Best Mom Ever print" style="background:linear-gradient(90deg,#f4f4f4,#e2e2e2 60%,#f0d9b0)"></div>
  <p>Best Mom Ever Custom<br>Photo Mug</p><a class="more">More Info</a>
</article>
<article class="abs product" style="left:477px">
  <div class="pic" role="img" aria-label="Laptop sleeve printed with a pet photo" style="background:linear-gradient(#9a7f62,#6b5a48 70%,#1d1d1d)"></div>
  <p>Custom Laptop Case<br>Keep your laptop safe</p><a class="more">More Info</a>
</article>
<article class="abs product" style="left:673px">
  <div class="pic" role="img" aria-label="Purple pullover hoodie" style="background:radial-gradient(ellipse at 50% 50%,#4a2f8f,#2f1c66 65%,#fff 66%)"></div>
  <p>Custom mediumweight<br>heavyweight. Choose</p><a class="more">More Info</a>
</article>

<div class="abs shadow-rule"></div>
<h2 class="abs section-title" style="top:873px;font-size:14.5px;font-weight:400">Customer Testimonials</h2>

<div class="abs quote" style="left:86px;top:905px">
  <div class="avatar" role="img" aria-label="Customer portrait"></div>
  <p>Lorem Ipsum is simply dummy text of the printing and typesetting industry. Lorem Ipsum has been the industry's standard dummy text ever since the 1500s, when an known<br>printer took a galley</p>
  <b>Jordan Hale</b><span>CEO, Founder</span>
</div>
<div class="abs quote" style="left:507px;top:905px">
  <div class="avatar" role="img" aria-label="Customer portrait"></div>
  <p style="width:270px">Lorem Ipsum is simply dummy text of the printing and typesetting industry. Lorem Ipsum has been the industry standard dummy text ever since the 1500s, when an known printer took a galley</p>
  <b>Jordan Hale</b><span>CEO, Founder</span>
</div>
<div class="abs t-dots"><i></i><i></i><i></i></div>

<footer class="abs footer"></footer>
<div class="abs f-col" style="left:85px"><h4>Products</h4><ul><li>Photo Books</li><li>Cards</li><li>Calendars</li><li>Photo Gifts</li><li>Collage Products</li></ul></div>
<div class="abs f-col" style="left:213px"><h4>About Us</h4><ul><li>About Us</li><li>Our Staff</li><li>Privacy Policy</li><li>Terms &amp; Conditions</li></ul></div>
<div class="abs f-col" style="left:350px"><h4>Account</h4><ul><li>My Account</li><li>Login / Register</li><li>Order Status</li><li>FAQ / Help</li></ul></div>
<div class="abs f-col" style="left:481px"><h4>Information</h4><ul><li>Help</li><li>Terms of Service</li><li>Privacy</li><li>Pricing</li><li>Sitemap</li></ul></div>
<div class="abs offer">
  <svg width="40" height="40" viewBox="0 0 40 40"><g transform="rotate(-30 20 20)"><rect x="4" y="10" width="32" height="21" fill="#f3ecd8" stroke="#c9bfa3"/><path d="M4 10l16 12 16-12" fill="none" stroke="#c9bfa3"/></g></svg>
  <span>Get Great Offers By Email!</span>
</div>
<div class="abs social"><h4>Follow Us</h4><ul><li><i></i>Friendwall</li><li><i></i>Chirpline</li><li><i></i>ClipStream</li></ul></div>
<div class="abs bottom-bar">Copyright © 2014 SnapGlo. All Rights Reserved</div>

</body>
</html>
```